Graphic design for Student Conference

We need design work done for our annual student conference called Lantern Fest. We have a central logo but need design work done to use on posters, banners, etc. that tie into the theme for this year's conference. The theme is "Be Glad" and I would like the design elements to have a very fun, 1980's or 1990's vibe to them. The feeling of happiness and joy should be felt in the design.

Target Market(s)

Students 10-12 years of age

Industry/Entity Type

Church

Requirements
Must have
• Must include the Lantern Fest logo - event date: June 19-21 - event website: brightoakparish.org/lanternfest - Flexible supporting artwork elements that can be used in a variety of mediums. - Must use fonts that are available from free, open sources or can be provided upon delivery of completed project.
Should not have
• Anything crude, scary or content inappropriate for middle school students. Should not have any imagery related to a classroom or meeting.

```html
<!DOCTYPE html>
<html lang="en">
<head>
<meta charset="utf-8">
<title>Lantern Fest — Annual Student Conference</title>
<link rel="stylesheet" href="https://fonts.googleapis.com/css2?family=Anton&family=Inter:wght@700;800;900&display=swap">
<style>
  :root {
    --sun: #f6e43a;
    --sky: #5c93e0;
    --ink: #0c0c0c;
    --photo-warm: #b58a6a;
    --photo-deep: #5a4a3a;
    --photo-green: #7c8a5a;
  }
  * { margin: 0; padding: 0; box-sizing: border-box; }
  html, body { width: 822px; height: 1200px; overflow: hidden; background: var(--sun); }
  .poster {
    position: relative;
    width: 822px;
    height: 1200px;
    overflow: hidden;
    background: var(--sun);
    color: var(--ink);
    font-family: "Inter", Arial, sans-serif;
  }
  .photo {
    position: absolute;
    left: 0; top: 432px;
    width: 822px; height: 678px;
    background:
      radial-gradient(ellipse at 25% 30%, #d7b497 0%, transparent 45%),
      radial-gradient(ellipse at 70% 75%, #c69c7c 0%, transparent 50%),
      linear-gradient(180deg, var(--photo-green) 0%, var(--photo-warm) 35%, var(--photo-deep) 100%);
  }
  .sky-band {
    position: absolute;
    left: 688px; top: 0;
    width: 134px; height: 779px;
    background: var(--sky);
  }
  .headline {
    position: absolute;
    left: -6px;
    font-weight: 900;
    font-size: 176px;
    line-height: 1;
    letter-spacing: -10px;
    white-space: nowrap;
  }
  .headline--top { top: -52px; }
  .headline--bottom { top: 96px; }
  .kicker {
    position: absolute;
    left: 24px; top: 271px;
    font-weight: 800;
    font-size: 23px;
    letter-spacing: -0.2px;
    white-space: nowrap;
  }
  .welcome {
    position: absolute;
    left: 25px; top: 309px;
    font-weight: 800;
    font-size: 19.5px;
    line-height: 20px;
  }
  .dates {
    position: absolute;
    left: 434px; top: 300px;
    font-family: "Anton", Impact, sans-serif;
    font-size: 104px;
    line-height: 1;
    letter-spacing: -1px;
    white-space: nowrap;
    transform: scaleX(0.82);
    transform-origin: left top;
  }
  .theme-title {
    position: absolute;
    left: 690px; top: 445px;
    height: 731px;
    width: 124px;
    writing-mode: vertical-rl;
    transform: rotate(180deg);
    font-weight: 900;
    font-size: 162px;
    line-height: 124px;
    letter-spacing: -4px;
    text-align: left;
    white-space: nowrap;
  }
  .theme-label {
    position: absolute;
    left: 650px; top: 994px;
    height: 182px;
    width: 32px;
    writing-mode: vertical-rl;
    transform: rotate(180deg);
    font-weight: 800;
    font-size: 36px;
    line-height: 32px;
    letter-spacing: 1px;
    white-space: nowrap;
  }
  .event-mark {
    position: absolute;
    left: 28px; top: 1064px;
    display: flex;
    align-items: center;
    gap: 12px;
    font-weight: 900;
    font-size: 38px;
    color: var(--ink);
    white-space: nowrap;
  }
  .event-mark__square {
    width: 26px; height: 26px;
    background: var(--ink);
  }
  .website {
    position: absolute;
    left: 0; width: 822px; top: 1158px;
    text-align: center;
    font-family: "Anton", Impact, sans-serif;
    font-size: 24px;
    letter-spacing: 0.2px;
    white-space: nowrap;
  }
</style>
</head>
<body>
<main class="poster">
  <div class="photo" role="img" aria-label="Photo of a crowd of smiling children making hand signs toward the camera"></div>
  <div class="sky-band"></div>

  <h1 class="headline headline--top">LANTERN</h1>
  <div class="headline headline--bottom">FEST</div>

  <p class="kicker">ANNUAL STUDENT CONFERENCE</p>
  <p class="welcome">We welcome<br>you to this<br>year’s<br>Lantern<br>Fest,</p>

  <p class="dates">June 19-21</p>

  <p class="theme-label">THEME</p>
  <p class="theme-title">BE GLAD</p>

  <div class="event-mark">
    <span class="event-mark__square"></span>
    <span>Lantern Fest</span>
  </div>

  <p class="website">brightoakparish.org/lanternfest</p>
</main>
</body>
</html>
```